Business Card Design Project

I would like a business card created for a new company. This is a holding company that acts as my investment company. It holds real estate and service based companies. The name of the company is Lucernaria which is Italian for Lanternry. Defined as development or growth.
We currently have no logo. I really like some of the "different" cards out there. Potentially metallic or grey/black. That looks premium/hi-end and unique. I am not sure if your design would be specific to the card stock I end with our just logo/design/font.
Real Estate

```html
<!DOCTYPE html>
<html lang="en">
<head>
<meta charset="utf-8">
<title>Lucernaria Real Estate — Business Card</title>
<link rel="stylesheet" href="https://fonts.googleapis.com/css2?family=Share+Tech+Mono&display=swap">
<style>
  :root {
    --stage: #262626;
    --navy: #141c45;
    --navy-deep: #0c1130;
    --ink: #0b0b0d;
    --ink-soft: #151517;
    --silhouette: #101013;
    --rule: #27306a;
    --text-light: #e6e6e6;
    --text-mid: #9a9a9a;
    --text-dim: #8a8a8a;
    --frame: #8c8c92;
    --mark-grey: #7c7f83;
  }
  html, body {
    margin: 0;
    padding: 0;
    width: 1200px;
    height: 1200px;
    overflow: hidden;
    background: var(--stage);
    font-family: "Share Tech Mono", monospace;
  }
  .canvas {
    position: relative;
    width: 1200px;
    height: 1200px;
  }
  .card {
    position: absolute;
    top: 190px;
    width: 470px;
    height: 820px;
    box-shadow: 0 20px 50px rgba(0,0,0,0.55);
    overflow: hidden;
  }
  /* ---------- Back card ---------- */
  .card--back {
    left: 80px;
    background: linear-gradient(180deg, var(--navy) 0%, var(--navy-deep) 30%, var(--ink-soft) 55%, var(--ink) 100%);
  }
  .skyline {
    position: absolute;
    left: 50px;
    top: 50px;
    width: 420px;
    height: 150px;
    background: linear-gradient(180deg, rgba(16,16,19,0.4) 0%, var(--silhouette) 60%, var(--silhouette) 100%);
  }
  .skyline--reflection {
    top: 212px;
    height: 120px;
    background: linear-gradient(180deg, var(--silhouette) 0%, rgba(16,16,19,0.55) 60%, rgba(16,16,19,0) 100%);
  }
  .band-rule {
    position: absolute;
    left: 50px;
    right: 0;
    height: 1px;
    background: var(--rule);
  }
  .band-rule--top { top: 208px; }
  .band-rule--contact { top: 522px; left: 60px; right: 0; }
  .band-rule--name { top: 572px; left: 190px; right: 0; }
  .brand-lockup {
    position: absolute;
    right: 88px;
    top: 164px;
    text-align: right;
    color: var(--text-light);
    font-size: 27px;
    letter-spacing: 3px;
    line-height: 40px;
  }
  .brand-lockup__line { display: block; height: 40px; }
  .brand-lockup__line + .brand-lockup__line { margin-top: 10px; }
  .contact {
    position: absolute;
    right: 22px;
    top: 530px;
    text-align: right;
    color: var(--text-mid);
    letter-spacing: 2px;
  }
  .contact__name { color: var(--text-light); font-size: 28px; line-height: 40px; }
  .contact__title { font-size: 23px; line-height: 30px; margin-top: 6px; margin-bottom: 16px; }
  .contact__address { font-size: 25px; line-height: 30px; margin-bottom: 20px; color: var(--text-dim); }
  .contact__phone { font-size: 23px; line-height: 27px; }
  .contact__phone b { font-weight: normal; font-size: 19px; }
  .contact__email { font-size: 24px; margin-top: 20px; }
  /* ---------- Front card ---------- */
  .card--front {
    left: 650px;
    background: linear-gradient(180deg, var(--navy) 0%, var(--navy-deep) 40%, var(--ink-soft) 75%, var(--ink) 100%);
  }
  .card__frame {
    position: absolute;
    inset: 12px;
    border: 2px solid var(--frame);
  }
  .mark {
    position: absolute;
    top: 130px;
    left: 0;
    right: 0;
    display: flex;
    align-items: center;
    justify-content: center;
    gap: 16px;
  }
  .mark__square {
    width: 44px;
    height: 44px;
    background: var(--mark-grey);
  }
  .mark__name {
    color: var(--text-light);
    font-size: 32px;
    letter-spacing: 4px;
  }
  .skyline--faint {
    left: 30px;
    top: 640px;
    width: 410px;
    height: 70px;
    background: linear-gradient(180deg, rgba(20,20,24,0) 0%, rgba(20,20,24,0.7) 100%);
  }
  .front-tagline {
    position: absolute;
    left: 0;
    right: 0;
    top: 735px;
    text-align: center;
    color: var(--text-light);
    font-size: 28px;
    letter-spacing: 3px;
  }
</style>
</head>
<body>
<main class="canvas">
  <section class="card card--back" aria-label="Card back">
    <div class="skyline" role="img" aria-label="City skyline silhouette"></div>
    <div class="skyline skyline--reflection" role="img" aria-label="Reflection of city skyline"></div>
    <div class="band-rule band-rule--top"></div>
    <div class="brand-lockup">
      <span class="brand-lockup__line">LUCERNARIA</span>
      <span class="brand-lockup__line">REAL ESTATE</span>
    </div>
    <div class="band-rule band-rule--contact"></div>
    <div class="band-rule band-rule--name"></div>
    <div class="contact">
      <div class="contact__name">MARCO BELLANDI</div>
      <div class="contact__title">JOB TITLE</div>
      <div class="contact__address">STREET NAME 1<br>CITY</div>
      <div class="contact__phone"><b>PHONE:</b>385.91.4620.318</div>
      <div class="contact__phone"><b>CELL:</b>385.91.4620.318</div>
      <div class="contact__email">M.BELLANDI@POSTMAIL.COM</div>
    </div>
  </section>

  <section class="card card--front" aria-label="Card front">
    <div class="card__frame"></div>
    <div class="mark">
      <span class="mark__square"></span>
      <span class="mark__name">LUCERNARIA</span>
    </div>
    <div class="skyline skyline--faint" role="img" aria-label="Faint city skyline silhouette"></div>
    <div class="front-tagline">REAL ESTATE</div>
  </section>
</main>
</body>
</html>
```